Business Card Design

I am a video director/cameraman and photographer. I cover documentaries, corporate, government departments, educational and non profits. They could be on Tv, Vidzio or DVD to 10 or 10 thousand ppl. Some have been seen worldwide and won international awards.
I regard myself as bold and saturated...as in I want strong ideas of substance to come through in a film and that the info is valid, interesting and saturates the mind without it being geeky boring.
Need a great logo and layout for cards. My name is Lionel Brastow and my company is TV Media Productions.

Must have company name, my name, email, website, phone and type of films I do. I'll supply additional info for the back- which will be companies I have filmed for.

Attach image shows I like the boxes/icons idea but am open to yr ideas...Roar on!
Updates

Project Deadline Extended
Reason: I am charged by your designs. This is the first time I have used ths type of service and getting to know you guys is very good value for me. Please keep your creative spirit in this. I want a contemporary logo. Some have shown the way forward and a few need to show a clean, current looking image of my attitude by way of log and design. Thx to you all Leo

Industry/Entity Type

Government

```html
<!DOCTYPE html>
<html lang="en">
<head>
<meta charset="utf-8">
<title>TV Media Productions – Business Card</title>
<link rel="stylesheet" href="https://fonts.googleapis.com/css2?family=Open+Sans:wght@400;600;700&family=Questrial&display=swap">
<style>
  :root {
    --backdrop: #4a3323;
    --card-white: #ffffff;
    --band-yellow: #f6c21a;
    --band-yellow-light: #fad449;
    --brand-red: #e8232a;
    --ink: #141414;
  }
  html, body {
    margin: 0;
    width: 1200px;
    height: 900px;
    overflow: hidden;
    background: var(--backdrop);
  }
  .card {
    position: absolute;
    left: 120px;
    top: 175px;
    width: 960px;
    height: 550px;
    background: var(--card-white);
    box-shadow: 0 14px 40px rgba(0,0,0,0.45);
    font-family: "Open Sans", Arial, sans-serif;
    color: var(--ink);
  }
  .card__header {
    position: absolute;
    inset: 0 0 auto 0;
    height: 228px;
    background: var(--card-white);
    border-bottom: 4px solid var(--ink);
  }
  .brand-mark {
    position: absolute;
    left: 60px;
    top: 118px;
    display: flex;
    align-items: center;
    gap: 16px;
  }
  .brand-mark__dot {
    width: 70px;
    height: 70px;
    border-radius: 50%;
    background: var(--ink);
  }
  .brand-mark__name {
    font-family: "Questrial", Arial, sans-serif;
    font-size: 40px;
    color: var(--ink);
    letter-spacing: 1px;
  }
  .company-name {
    position: absolute;
    right: 70px;
    top: 42px;
    margin: 0;
    text-align: left;
    font-family: "Questrial", Arial, sans-serif;
    font-weight: 400;
    font-size: 50px;
    line-height: 54px;
    letter-spacing: 2px;
    color: var(--brand-red);
    text-transform: uppercase;
  }
  .card__body {
    position: absolute;
    inset: 232px 0 0 0;
    background: linear-gradient(100deg, var(--band-yellow) 0%, var(--band-yellow) 55%, var(--band-yellow-light) 100%);
  }
  .person-name {
    position: absolute;
    left: 110px;
    top: 118px;
    margin: 0;
    font-size: 27px;
    font-weight: 700;
    letter-spacing: 1px;
    text-transform: uppercase;
  }
  .divider {
    position: absolute;
    left: 455px;
    top: 26px;
    width: 4px;
    height: 190px;
    background: var(--ink);
  }
  .contact {
    position: absolute;
    left: 500px;
    top: 22px;
    margin: 0;
    padding: 0;
    list-style: none;
    font-size: 21px;
    line-height: 28px;
  }
  .contact li {
    display: flex;
    align-items: flex-start;
    gap: 14px;
  }
  .contact li.contact__address { margin-top: 20px; }
  .contact svg {
    width: 16px;
    height: 16px;
    margin-top: 6px;
    flex: none;
    fill: var(--ink);
  }
  .film-types {
    position: absolute;
    left: 0;
    right: 0;
    top: 250px;
    margin: 0;
    text-align: center;
    font-size: 17px;
    font-weight: 600;
    letter-spacing: 2px;
    text-transform: uppercase;
    color: var(--ink);
  }
</style>
</head>
<body>
  <article class="card">
    <header class="card__header">
      <div class="brand-mark">
        <span class="brand-mark__dot"></span>
        <span class="brand-mark__name">TV Media</span>
      </div>
      <h1 class="company-name">TV Media<br>Productions</h1>
    </header>
    <section class="card__body">
      <p class="person-name">Lionel Brastow</p>
      <span class="divider"></span>
      <ul class="contact">
        <li>
          <svg viewBox="0 0 16 16" aria-hidden="true"><path d="M3.5 1l3 3-2 2c1 2 3 4 5 5l2-2 3 3-2 2.5C6 14 2 10 1 3.5z"/></svg>
          <span>+123 555 0190</span>
        </li>
        <li>
          <svg viewBox="0 0 16 16" aria-hidden="true"><path d="M1 3h14v10H1z M2 4l6 5 6-5" fill="none" stroke="#141414" stroke-width="1.6"/><path d="M1 3h14L8 8.5z"/></svg>
          <span>lionel@tvmediaprod.com</span>
        </li>
        <li>
          <svg viewBox="0 0 16 16" aria-hidden="true"><circle cx="10" cy="6" r="4" fill="none" stroke="#141414" stroke-width="2"/><path d="M7 9l-5 5" stroke="#141414" stroke-width="2.4"/></svg>
          <span>www.tvmediaprod.com</span>
        </li>
        <li class="contact__address">
          <svg viewBox="0 0 16 16" aria-hidden="true"><path d="M8 1l7 7h-2v7H9.5v-4h-3v4H3V8H1z"/></svg>
          <span>51, Marlow Lane,<br>Ashford</span>
        </li>
      </ul>
      <p class="film-types">Documentaries · Corporate · Government · Educational · Non-Profit</p>
    </section>
  </article>
</body>
</html>
```